School Leavers Brochure 2020/21

We require an all new brochure for School Leavers tee shirts and hoodies.
Updates

Pitchforge only gave about 24-48 hour deadline from the time i posted the project

Target Market(s)

Schools

Font styles to use
Sans Serif

Colors
3276b5

Requirements
Must have
• information about KAL, see current flyer.
• services for leavers garments :
• Screen printing
• Fully Sublimated
• Individual names
• Embroidered or printed school logo
• Choose from a template or send us a drawing of your idea
• Hundreds of different tees, hoodies and polos to choose from
• www.kestrelathleticlane.com.au/catalogues
• step 1 : Choose your garment
• step 2 : Let us know your print requirements and /or logo required
• step 3 : email us for a quote
• step 4 : Order
• I don't mind if number of pages has to increase, but it has to be suitable to both email and post.
Nice to have
• essentially we require different print ideas that we can present to Schools to entice them to buy from us.
• the flyer attached works ok, but maybe we should advertise the fact that we can do many different colours of tees, polo shirts and hoodies being the main product a School will but with theire leavers print
• we have a website with numerous catalogues that we can screenprint designs onto.

```html
<!DOCTYPE html>
<html lang="en">
<head>
<meta charset="utf-8">
<title>KAL – School Leavers Brochure</title>
<link rel="stylesheet" href="https://fonts.googleapis.com/css2?family=Montserrat:wght@600;700;800&family=Lato:wght@400;700&display=swap">
<style>
  :root {
    --stage: #3a3a3a;
    --black: #0d0d0d;
    --charcoal: #2a2a2a;
    --white: #ffffff;
    --paper: #f2f2f2;
    --grey: #cfcfcf;
    --light-grey: #d9d9d9;
    --orange: #f15a24;
    --red: #e03a1e;
    --deep-red: #c1271a;
    --heading: "Montserrat", Arial, sans-serif;
    --body: "Lato", Arial, sans-serif;
  }
  * { box-sizing: border-box; margin: 0; padding: 0; }
  html, body { width: 1200px; height: 1200px; overflow: hidden; background: var(--stage); }
  .canvas { position: relative; width: 1200px; height: 1200px; background: var(--stage); font-family: var(--body); }

  .spread { position: absolute; overflow: hidden; }
  .spread-cover { left: 216px; top: 78px; width: 744px; height: 520px; }
  .spread-inside { left: 214px; top: 622px; width: 746px; height: 524px; }
  .spread > svg.backdrop { position: absolute; inset: 0; }

  .brand { position: absolute; display: flex; align-items: center; gap: 8px; font-family: var(--heading); font-weight: 800; line-height: 1; }
  .brand .mark { display: block; border-radius: 50%; background: var(--red); }
  .brand-back { left: 118px; top: 140px; font-size: 48px; color: var(--black); }
  .brand-back .mark { width: 16px; height: 16px; }
  .brand-front { left: 614px; top: 48px; font-size: 34px; color: var(--black); }
  .brand-front .mark { width: 12px; height: 12px; }
  .brand-inside { left: 512px; top: 196px; font-size: 38px; color: var(--white); }
  .brand-inside .mark { width: 13px; height: 13px; }

  .follow { position: absolute; left: 10px; top: 462px; display: flex; align-items: center; gap: 6px; color: var(--white); font-size: 11px; }
  .follow .square { width: 11px; height: 11px; background: var(--white); border-radius: 2px; }
  .web { position: absolute; font-family: var(--heading); font-weight: 700; color: var(--white); letter-spacing: 0.3px; }
  .web-back { left: 10px; top: 484px; font-size: 15px; }
  .web-front { left: 390px; top: 481px; font-size: 14px; display: flex; align-items: center; gap: 6px; }

  .hero-garment { position: absolute; left: 430px; top: 100px; width: 228px; height: 250px; }
  .cover-title { position: absolute; left: 388px; top: 380px; font-family: var(--heading); font-weight: 800; font-size: 42px; line-height: 1.02; color: var(--light-grey); letter-spacing: 1.5px; }

  .services-title { position: absolute; left: 20px; top: 54px; width: 286px; text-align: center; font-family: var(--heading); font-weight: 700; font-size: 21px; line-height: 1.25; color: var(--white); letter-spacing: 1px; }

  .steps { position: absolute; left: 410px; top: 30px; list-style: none; color: var(--white); font-size: 14px; }
  .steps li { display: flex; align-items: flex-start; gap: 8px; margin-bottom: 10px; line-height: 1.25; }
  .steps .badge { flex: none; background: var(--orange); color: var(--white); padding: 1px 5px; border-radius: 3px; }

  .checklist { position: absolute; list-style: none; font-size: 11px; color: var(--black); }
  .checklist li { display: flex; gap: 3px; line-height: 1.15; margin-bottom: 14px; }
  .checklist svg { flex: none; margin-top: 1px; }
  .checklist-a { left: 10px; top: 217px; width: 130px; }
  .checklist-a li { margin-bottom: 16px; }
  .checklist-b { left: 150px; top: 216px; width: 200px; }
  .checklist-b li { margin-bottom: 8px; }

  .catalogue-link { position: absolute; left: 32px; top: 309px; display: flex; align-items: center; gap: 4px; }
  .catalogue-link .pill { background: var(--red); color: var(--white); font-size: 11px; padding: 2px 7px; border-radius: 9px; }

  .design-grid { position: absolute; left: 20px; top: 334px; width: 300px; display: grid; grid-template-columns: repeat(4, 1fr); row-gap: 6px; }
  .design-card { height: 90px; display: flex; flex-direction: column; align-items: center; justify-content: flex-end; border-right: 1px solid #e4e4e4; padding-bottom: 2px; }
  .design-card .garment { width: 58px; height: 66px; border-radius: 14px 14px 4px 4px; background: linear-gradient(#2b2b2b, var(--black)); }
  .design-card .label { font-family: var(--heading); font-weight: 700; font-size: 5px; color: #444; margin-top: 3px; letter-spacing: 0.3px; }

  .diy { position: absolute; left: 612px; top: 384px; font-family: var(--heading); font-weight: 800; font-size: 23px; line-height: 1.18; color: var(--black); }
  .diy .accent { display: block; background: var(--orange); color: var(--white); padding-left: 4px; margin-left: -4px; width: 142px; }
</style>
</head>
<body>
<main class="canvas">

  <section class="spread spread-cover">
    <svg class="backdrop" width="744" height="520" viewBox="0 0 744 520">
      <defs>
        <linearGradient id="coverRed" x1="0" y1="0" x2="1" y2="1">
          <stop offset="0" stop-color="var(--deep-red)"/>
          <stop offset="0.6" stop-color="var(--orange)"/>
          <stop offset="1" stop-color="var(--red)"/>
        </linearGradient>
        <linearGradient id="coverArc" x1="0" y1="0" x2="1" y2="0">
          <stop offset="0" stop-color="#f47a30"/>
          <stop offset="1" stop-color="var(--red)"/>
        </linearGradient>
        <linearGradient id="coverLight" x1="0" y1="0" x2="1" y2="0">
          <stop offset="0" stop-color="#d2d2d2"/>
          <stop offset="0.5" stop-color="#f4f4f4"/>
          <stop offset="1" stop-color="#ffffff"/>
        </linearGradient>
      </defs>
      <rect width="374" height="520" fill="var(--black)"/>
      <path d="M272,0 L374,0 L374,520 L352,520 C220,440 60,360 36,260 C14,160 140,50 272,0 Z" fill="var(--white)"/>
      <path d="M360,0 L374,0 L374,520 L350,520 C280,440 252,330 268,220 C282,120 320,50 360,0 Z" fill="url(#coverArc)"/>
      <rect x="374" width="370" height="520" fill="url(#coverRed)"/>
      <path d="M588,0 L744,0 L744,410 C640,385 520,355 440,325 C392,302 372,240 374,180 C378,110 470,40 588,0 Z" fill="url(#coverLight)"/>
    </svg>

    <div class="brand brand-back"><span class="mark"></span>KAL</div>
    <div class="follow">Follow us on <span class="square"></span></div>
    <div class="web web-back">www.kestrelathleticlane.com.au</div>

    <div class="brand brand-front"><span class="mark"></span>KAL</div>
    <svg class="hero-garment" role="img" aria-label="Back view of a black hoodie with a School Leavers '19 print" viewBox="0 0 228 250">
      <rect width="228" height="250" rx="40" fill="#161616"/>
    </svg>
    <h1 class="cover-title">SCHOOL<br>LEAVERS</h1>
    <div class="web web-front">
      <svg width="13" height="13" viewBox="0 0 14 14" fill="none" stroke="#fff" stroke-width="1.2"><circle cx="7" cy="7" r="6"/><ellipse cx="7" cy="7" rx="2.6" ry="6"/><line x1="1" y1="7" x2="13" y2="7"/></svg>
      www.kestrelathleticlane.com.au
    </div>
  </section>

  <section class="spread spread-inside">
    <svg class="backdrop" width="746" height="524" viewBox="0 0 746 524">
      <defs>
        <linearGradient id="insideDark" x1="0" y1="0" x2="1" y2="0">
          <stop offset="0" stop-color="var(--black)"/>
          <stop offset="0.6" stop-color="var(--charcoal)"/>
          <stop offset="1" stop-color="var(--black)"/>
        </linearGradient>
        <linearGradient id="insideWave" x1="0" y1="0" x2="1" y2="0">
          <stop offset="0" stop-color="var(--orange)"/>
          <stop offset="0.5" stop-color="var(--red)"/>
          <stop offset="1" stop-color="var(--orange)"/>
        </linearGradient>
        <linearGradient id="insidePaper" x1="0" y1="0" x2="1" y2="0">
          <stop offset="0" stop-color="var(--white)"/>
          <stop offset="1" stop-color="var(--grey)"/>
        </linearGradient>
        <linearGradient id="photoTone" x1="0" y1="0" x2="1" y2="1">
          <stop offset="0" stop-color="#8fb2c0"/>
          <stop offset="0.5" stop-color="#b9cfd8"/>
          <stop offset="1" stop-color="#7fa3b3"/>
        </linearGradient>
      </defs>
      <rect width="746" height="524" fill="url(#insideDark)"/>
      <path d="M0,102 C20,170 60,200 120,190 C170,180 200,136 250,134 C330,132 380,230 470,258 C560,282 680,240 746,262 L746,524 L0,524 Z" fill="url(#insideWave)"/>
      <path d="M0,196 C90,200 170,162 250,146 C310,134 345,164 374,208 L374,524 L0,524 Z" fill="url(#insidePaper)"/>
      <g role="img" aria-label="Photo of a man wearing a plain white t-shirt against a pale blue wall">
        <path d="M374,276 C430,300 500,306 560,296 C630,284 690,306 746,366 L746,524 L374,524 Z" fill="url(#photoTone)"/>
        <path d="M374,306 C410,314 460,322 500,318 L518,524 L374,524 Z" fill="#eeeeee"/>
      </g>
      <path d="M705,524 C720,480 735,440 746,420 L746,524 Z" fill="var(--orange)"/>
    </svg>

    <h2 class="services-title">SERVICES FOR<br>LEAVERS GARMENTS</h2>

    <ol class="steps">
      <li><span class="badge">step 1</span><span>: Choose your garment</span></li>
      <li><span class="badge">step 2</span><span>: Let us know your print requirements and<br>&nbsp;/or&nbsp; logo&nbsp; required</span></li>
      <li><span class="badge">step 3</span><span>: Email us for a quote</span></li>
      <li><span class="badge">step 4</span><span>: Order</span></li>
    </ol>

    <div class="brand brand-inside"><span class="mark"></span>KAL</div>

    <ul class="checklist checklist-a">
      <li><svg width="12" height="11" viewBox="0 0 12 11" fill="none" stroke="#111" stroke-width="1.2"><rect x="0.6" y="1.6" width="8.5" height="8.5"/><path d="M2.5,5.5 L5,8 L11.4,0.6"/></svg>Screen printing</li>
      <li><svg width="12" height="11" viewBox="0 0 12 11" fill="none" stroke="#111" stroke-width="1.2"><rect x="0.6" y="1.6" width="8.5" height="8.5"/><path d="M2.5,5.5 L5,8 L11.4,0.6"/></svg>Fully Sublimated</li>
      <li><svg width="12" height="11" viewBox="0 0 12 11" fill="none" stroke="#111" stroke-width="1.2"><rect x="0.6" y="1.6" width="8.5" height="8.5"/><path d="M2.5,5.5 L5,8 L11.4,0.6"/></svg>Individual names</li>
    </ul>
    <ul class="checklist checklist-b">
      <li><svg width="12" height="11" viewBox="0 0 12 11" fill="none" stroke="#111" stroke-width="1.2"><rect x="0.6" y="1.6" width="8.5" height="8.5"/><path d="M2.5,5.5 L5,8 L11.4,0.6"/></svg><span>Embroidered or printed<br>school logo</span></li>
      <li><svg width="12" height="11" viewBox="0 0 12 11" fill="none" stroke="#111" stroke-width="1.2"><rect x="0.6" y="1.6" width="8.5" height="8.5"/><path d="M2.5,5.5 L5,8 L11.4,0.6"/></svg><span>Choose from a template or send us a<br>drawing of your idea</span></li>
      <li><svg width="12" height="11" viewBox="0 0 12 11" fill="none" stroke="#111" stroke-width="1.2"><rect x="0.6" y="1.6" width="8.5" height="8.5"/><path d="M2.5,5.5 L5,8 L11.4,0.6"/></svg><span>Hundreds of different tees, hoodies<br>and polos to choose from</span></li>
    </ul>

    <div class="catalogue-link">
      <svg width="18" height="18" viewBox="0 0 18 18" fill="none"><circle cx="9" cy="9" r="8.3" stroke="var(--red)" stroke-width="1"/><g stroke="#111" stroke-width="1"><circle cx="9" cy="9" r="5.5"/><ellipse cx="9" cy="9" rx="2.3" ry="5.5"/><line x1="3.5" y1="9" x2="14.5" y2="9"/></g></svg>
      <span class="pill">www.kestrelathleticlane.com.au/catalogues</span>
    </div>

    <div class="design-grid">
      <div class="design-card"><div class="garment" role="img" aria-label="Black hoodie with class of 2019 print"></div><span class="label">DESIGN 17</span></div>
      <div class="design-card"><div class="garment" role="img" aria-label="Black hoodie with large 19 print"></div><span class="label">DESIGN 18</span></div>
      <div class="design-card"><div class="garment" role="img" aria-label="Black hoodie with 2019 leavers print"></div><span class="label">DESIGN 19</span></div>
      <div class="design-card"><div class="garment" role="img" aria-label="Black hoodie with 19 leavers print"></div><span class="label">DESIGN 20</span></div>
      <div class="design-card"><div class="garment" role="img" aria-label="Black hoodie with class of 19 leavers print"></div><span class="label">DESIGN 21</span></div>
      <div class="design-card"><div class="garment" role="img" aria-label="Black hoodie with name and 19 leavers print"></div><span class="label">DESIGN 22</span></div>
      <div class="design-card"><div class="garment" role="img" aria-label="Black hoodie with two thousand nineteen print"></div><span class="label">DESIGN 23</span></div>
      <div class="design-card"><div class="garment" role="img" aria-label="Black hoodie with vertical 2019 leavers print"></div><span class="label">DESIGN 24</span></div>
    </div>

    <p class="diy"><span class="accent">DESIGN</span>YOUR<br>OWN</p>
  </section>

</main>
</body>
</html>
```